Business Card design for a skin clinic

i would like a business card design for our skin clinic.
our logo colors are Blue and Grey and Bule /white.
we are searching for a minimalistic design yet very elegant,dynamic and professional which can reflect a professional medical skin care clinic( not a beauty salon).
THE DESGIN IS NOT FOR A PERSON IT WILL BE USED IN THE CLINIC FOR CLIENTS SO THERE SHOULD BE NO NAME OF A PERSON ONLY THE CLINIC NAME AND THE CONTACT INFO

Target Market(s)
young and old womens
Industry/Entity Type
Business
Contact Information for Business Card
we have 2 address and both should be on the card.
address A: Lindenhofkade 42B, 3017KP Rotterdam, Tel 010 438 21 95
address B: Zonnewijzerstraat 73, 1062HT Amsterdam Tel 020 519 8372
website www.velorahuid.nu, email info@velorahuid.nu
Look and feel

```html
<!DOCTYPE html>
<html lang="nl">
<head>
<meta charset="utf-8">
<title>Velorahuid – business card</title>
<link rel="stylesheet" href="https://fonts.googleapis.com/css2?family=Montserrat:wght@500&family=Open+Sans:wght@400;600&display=swap">
<style>
  :root {
    --page: #e9eaec;
    --card-dark: #2b2b2e;
    --card-light: #ffffff;
    --blue: #1f72d8;
    --blue-light: #27a4e6;
    --grey: #55565b;
    --grey-text: #4a4b50;
    --tagline: #8a8b90;
    --white: #ffffff;
  }
  * { box-sizing: border-box; margin: 0; padding: 0; }
  html, body {
    width: 1200px; height: 977px; overflow: hidden;
    background: var(--page);
    font-family: "Open Sans", Arial, sans-serif;
  }
  .sheet {
    width: 1200px; height: 977px;
    display: flex; flex-direction: column; align-items: center; justify-content: center;
    gap: 57px;
  }
  .card {
    position: relative; width: 700px; height: 400px;
    box-shadow: 0 6px 18px rgba(0,0,0,.18);
    overflow: hidden;
  }
  /* back side */
  .card--back { background: var(--card-dark); display: flex; align-items: center; justify-content: center; }
  .brand { display: flex; flex-direction: column; align-items: flex-start; }
  .brand__row { display: flex; align-items: center; gap: 12px; }
  .brand__mark { width: 16px; height: 16px; background: var(--blue); }
  .brand__name {
    font-family: "Montserrat", Arial, sans-serif; font-weight: 500;
    letter-spacing: 3px; line-height: 1;
  }
  .brand__tagline {
    font-family: "Montserrat", Arial, sans-serif; font-weight: 500;
    letter-spacing: 1.5px; text-transform: lowercase;
  }
  .card--back .brand__name { color: var(--white); font-size: 40px; }
  .card--back .brand__tagline { color: #d8d9dc; font-size: 14px; margin: 10px 0 0 28px; }

  /* front side */
  .card--front { background: var(--card-light); }
  .card--front .brand { position: absolute; left: 78px; top: 78px; }
  .card--front .brand__name { color: var(--grey-text); font-size: 30px; }
  .card--front .brand__tagline { color: var(--tagline); font-size: 11px; margin: 8px 0 0 28px; }

  .corner-tab { position: absolute; right: 0; top: 52px; width: 30px; height: 36px; background: var(--blue); }

  .contact {
    position: absolute; left: 78px; top: 178px; width: 500px;
    display: grid; grid-template-columns: 250px 250px; row-gap: 8px;
    list-style: none;
  }
  .contact__item { display: flex; align-items: center; gap: 12px; color: var(--grey-text); font-size: 13px; line-height: 1.35; }
  .contact__icon { width: 14px; height: 14px; flex: none; fill: var(--blue); }

  .card__bands { position: absolute; left: 0; bottom: 0; width: 700px; height: 90px; }
</style>
</head>
<body>
<main class="sheet">
  <section class="card card--back" aria-label="Card back">
    <div class="brand">
      <div class="brand__row">
        <span class="brand__mark"></span>
        <span class="brand__name">VELORAHUID</span>
      </div>
      <span class="brand__tagline">next generation skin care</span>
    </div>
  </section>

  <section class="card card--front" aria-label="Card front">
    <div class="brand">
      <div class="brand__row">
        <span class="brand__mark"></span>
        <span class="brand__name">VELORAHUID</span>
      </div>
      <span class="brand__tagline">next generation skin care</span>
    </div>

    <span class="corner-tab"></span>

    <ul class="contact">
      <li class="contact__item">
        <svg class="contact__icon" viewBox="0 0 24 24"><path d="M12 2a7 7 0 0 0-7 7c0 5 7 13 7 13s7-8 7-13a7 7 0 0 0-7-7zm0 9.5A2.5 2.5 0 1 1 12 6.5a2.5 2.5 0 0 1 0 5z"/></svg>
        <span>Lindenhofkade 42B,<br>3017KP Rotterdam</span>
      </li>
      <li class="contact__item">
        <svg class="contact__icon" viewBox="0 0 24 24"><path d="M12 2a7 7 0 0 0-7 7c0 5 7 13 7 13s7-8 7-13a7 7 0 0 0-7-7zm0 9.5A2.5 2.5 0 1 1 12 6.5a2.5 2.5 0 0 1 0 5z"/></svg>
        <span>Zonnewijzerstraat 73,<br>1062HT Amsterdam</span>
      </li>
      <li class="contact__item">
        <svg class="contact__icon" viewBox="0 0 24 24"><path d="M6.6 10.8a15 15 0 0 0 6.6 6.6l2.2-2.2c.3-.3.7-.4 1-.2 1.1.4 2.3.6 3.6.6.6 0 1 .4 1 1V20c0 .6-.4 1-1 1A17 17 0 0 1 3 4c0-.6.4-1 1-1h3.5c.6 0 1 .4 1 1 0 1.3.2 2.5.6 3.6.1.3 0 .7-.2 1z"/></svg>
        <span>010 438 21 95</span>
      </li>
      <li class="contact__item">
        <svg class="contact__icon" viewBox="0 0 24 24"><path d="M6.6 10.8a15 15 0 0 0 6.6 6.6l2.2-2.2c.3-.3.7-.4 1-.2 1.1.4 2.3.6 3.6.6.6 0 1 .4 1 1V20c0 .6-.4 1-1 1A17 17 0 0 1 3 4c0-.6.4-1 1-1h3.5c.6 0 1 .4 1 1 0 1.3.2 2.5.6 3.6.1.3 0 .7-.2 1z"/></svg>
        <span>020 519 8372</span>
      </li>
      <li class="contact__item">
        <svg class="contact__icon" viewBox="0 0 24 24"><path d="M2 5h20v14H2z"/><path d="M2 6l10 7.5L22 6" fill="none" stroke="#fff" stroke-width="1.6"/></svg>
        <span>info@velorahuid.nu</span>
      </li>
      <li class="contact__item">
        <svg class="contact__icon" viewBox="0 0 24 24"><circle cx="12" cy="12" r="10"/><path d="M2 12h20M12 2c3 3 3 17 0 20M12 2c-3 3-3 17 0 20" fill="none" stroke="#fff" stroke-width="1.4"/></svg>
        <span>www.velorahuid.nu</span>
      </li>
    </ul>

    <svg class="card__bands" viewBox="0 0 700 90" aria-hidden="true">
      <defs>
        <linearGradient id="bandBlue" x1="0" x2="1" y1="0" y2="0">
          <stop offset="0" stop-color="#1f72d8"/>
          <stop offset="1" stop-color="#27a4e6"/>
        </linearGradient>
      </defs>
      <polygon points="0,64 226,64 240,90 0,90" fill="#55565b"/>
      <polygon points="248,90 234,66 640,8 640,90" fill="url(#bandBlue)"/>
      <polygon points="640,8 664,4 660,90 640,90" fill="#ffffff"/>
      <polygon points="664,4 700,0 700,90 652,90" fill="#55565b"/>
    </svg>
  </section>
</main>
</body>
</html>
```